Web design for Money Service Business (uncoded)

We need a very basic website with 5-6 pages. Home page, Services, Transfer(How to use our service), About us, Contact us, FAQ
Our company name is Harbin Coinage. We are a company that deals with currency exchange and international money transfer. We do cash exchange and international money transfers to bank accounts all over the world. We offer highly competitive exchange rates so usually attract customers who transfer money over $10,000. Our niche is with larger sums of money, the design needs to be professional and communicate trust, security and stability.
Industry/Entity Type
Security
Look and feel
Each slider illustrates characteristics of the customer's brand and the style your logo design should communicate.

```html
<!DOCTYPE html>
<html lang="en">
<head>
<meta charset="utf-8">
<title>Harbin Coinage — International Money Transfer</title>
<link href="https://fonts.googleapis.com/css2?family=Arimo:ital,wght@0,400;0,700;1,400&family=Questrial&display=swap" rel="stylesheet">
<style>
  :root {
    --navy: #0b4677;
    --navy-deep: #083a63;
    --cyan: #00a9d9;
    --steel: #3d73a6;
    --orange: #f7941d;
    --ink: #555;
    --title: #0f5a93;
    --panel-bg: #fbfbfb;
    --panel-line: #dcdcdc;
    --white: #fff;
  }
  * { box-sizing: border-box; margin: 0; padding: 0; }
  html, body { width: 1200px; height: 1000px; overflow: hidden; background: var(--white); }
  body { position: relative; font-family: "Arimo", Arial, sans-serif; color: var(--ink); }
  .abs { position: absolute; }

  /* header */
  .brand { left: 278px; top: 28px; }
  .brand-name { font-family: "Questrial", sans-serif; font-size: 34px; color: var(--navy); letter-spacing: 0.3px; line-height: 1; }
  .brand-tag { font-family: "Questrial", sans-serif; font-size: 13px; color: var(--steel); letter-spacing: 2px; margin-top: 7px; }
  .social { right: 210px; top: 33px; display: flex; gap: 5px; }
  .social span { width: 25px; height: 25px; border-radius: 50%; background: var(--navy); display: block; }

  /* nav */
  .nav { left: 0; top: 113px; width: 1200px; height: 32px; background: var(--navy); }
  .nav ul { list-style: none; position: absolute; left: 275px; top: 0; display: flex; height: 32px; }
  .nav li { font-size: 9px; color: var(--white); line-height: 32px; padding: 0 8px; }
  .nav li.active { background: var(--cyan); font-weight: 700; padding: 0 16px; margin-right: 2px; }
  .nav li.faq { margin-left: 16px; }

  /* hero */
  .hero-art { left: 400px; top: 145px; width: 650px; height: 233px; z-index: 0;
    background: linear-gradient(100deg, rgba(255,255,255,0) 0%, rgba(255,255,255,0) 20%, #c9d6f2 42%, #5f82cf 72%, #3c63bf 100%); }
  .hero-title, .hero-sub, .btn { z-index: 2; }
  .hero-title { left: 275px; top: 214px; font-family: "Questrial", sans-serif; font-size: 20px; color: var(--navy); line-height: 1.2; }
  .hero-sub { left: 275px; top: 276px; font-family: "Questrial", sans-serif; font-size: 18px; color: var(--orange); }
  .btn { left: 275px; top: 310px; width: 72px; height: 22px; border-radius: 3px; background: linear-gradient(#3f7db8, #1e5a92); color: var(--white); font-size: 9px; line-height: 22px; text-align: center; }

  /* bands */
  .stripe { left: 0; top: 383px; width: 1200px; height: 21px; background: var(--steel); }
  .band-cyan { left: 0; top: 404px; width: 1200px; height: 86px; background: linear-gradient(#13b8e6, #0a8cc6 45%, #0a5e9a); border-top: 2px solid #7fd7f2; }
  .band-navy { left: 0; top: 490px; width: 1200px; height: 56px; background: var(--navy); border-top: 2px solid #3aa6d4; }
  .band-heading { left: 289px; top: 429px; font-size: 11px; font-weight: 700; color: var(--white); }
  .band-art { left: 278px; top: 446px; width: 142px; height: 44px; border-radius: 70px 70px 0 0; background: linear-gradient(#9fd3ef, #2d7fc0); }
  .band-text { left: 459px; top: 417px; width: 540px; font-size: 10.5px; line-height: 1.25; color: var(--white); }
  .band-brand { left: 300px; top: 506px; font-family: "Questrial", sans-serif; font-size: 12px; color: var(--white); }
  .band-strong { left: 459px; top: 507px; font-size: 10.5px; font-weight: 700; color: var(--white); }

  /* content panel */
  .panel { left: 274px; top: 533px; width: 726px; height: 419px; background: var(--white); border-radius: 6px 6px 0 0; box-shadow: 0 0 10px rgba(0,0,0,0.18); }
  .feature { top: 555px; width: 227px; height: 193px; background: var(--panel-bg); border: 1px solid var(--panel-line); text-align: center; }
  .feature h3 { font-weight: 400; font-size: 11px; color: var(--title); margin-top: 17px; }
  .feature .art { width: 100px; height: 70px; margin: 10px auto 0; border-radius: 4px; }
  .feature p { font-size: 7px; line-height: 1.55; padding: 0 16px; margin-top: 14px; }
  .feature .more { display: block; font-size: 7px; font-weight: 700; color: #999; margin-top: 10px; }
  .feature .more.lit { color: var(--orange); text-decoration: underline; }
  .art-gears { background: linear-gradient(#f0f0f0, #d9473a); }
  .art-chart { background: linear-gradient(#f5f5f5, #6b8fd0); }
  .art-team { background: linear-gradient(#e8e8e8, #2a2a35); }

  .welcome { left: 286px; top: 792px; width: 460px; }
  .section-title { font-size: 11px; font-weight: 400; color: var(--title); }
  .welcome p { font-size: 7px; line-height: 1.6; margin-top: 13px; }
  .welcome p + p { margin-top: 10px; }
  .welcome a { color: var(--orange); text-decoration: underline; }
  .testimonial { left: 764px; top: 792px; width: 226px; }
  .quote { font-size: 8px; font-style: italic; line-height: 14px; color: #888; padding: 0 24px 0 23px; margin-top: 33px; position: relative; }
  .mark { position: absolute; font-family: Georgia, serif; font-size: 22px; color: #ccc; font-style: normal; }
  .testimonial .author { font-size: 8px; color: var(--title); text-align: right; margin-top: 24px; }

  /* footer */
  .footer { left: 0; top: 952px; width: 1200px; height: 48px; background: var(--navy-deep); border-top: 2px solid #2a8fc4; text-align: center; color: var(--white); }
  .footer .links { font-size: 7px; margin-top: 17px; }
  .footer .copy { font-size: 6px; margin-top: 5px; }
</style>
</head>
<body>

<header>
  <div class="abs brand">
    <div class="brand-name">HARBIN COINAGE</div>
    <div class="brand-tag">INTERNATIONAL MONEY TRANSFER</div>
  </div>
  <div class="abs social" aria-label="Social links"><span></span><span></span><span></span></div>
</header>

<nav class="abs nav">
  <ul>
    <li class="active">Home</li><li>Services</li><li>Transfer</li><li>About us</li><li>Contact us</li><li class="faq">FAQ</li>
  </ul>
</nav>

<section class="hero">
  <div class="abs hero-art" role="img" aria-label="Illustration of rising blue bar chart with currency dice and upward arrow"></div>
  <div class="abs hero-title">Transferring Money<br>Internationally?</div>
  <div class="abs hero-sub">Transfer money over $10,000</div>
  <div class="abs btn">Learn More</div>
</section>

<section class="bands">
  <div class="abs stripe"></div>
  <div class="abs band-cyan"></div>
  <div class="abs band-navy"></div>
  <div class="abs band-heading">HEADING GOES HERE</div>
  <div class="abs band-art" role="img" aria-label="Illustration of currency symbols on a globe"></div>
  <p class="abs band-text">Lorem ipsum dolor sit amet, consectetur adipisicing elit, sed do eiusmod tempor incididunt ut labore et dolore magna aliqua. Ut enim ad minim veniam, quis nostrud exercitation ullamco laboris nisi ut aliquip ex ea commodo consequat.</p>
  <div class="abs band-brand">HARBIN COINAGE</div>
  <p class="abs band-strong">Lorem ipsum dolor sit amet, consectetur adipisicing elit, sed do eiusmod tempor incididunt.</p>
</section>

<main>
  <div class="abs panel"></div>

  <article class="abs feature" style="left:285px">
    <h3>Solutions</h3>
    <div class="art art-gears" role="img" aria-label="Illustration of figures pushing red gears"></div>
    <p>Lorem ipsum dolor sit amet, consectetur adipisicing elit, sed do eiusmod tempor incididunt ut labore et dolore magna aliqua. Ut enim ad minim veniam, quis nostrud</p>
    <span class="more lit">read more &gt;&gt;</span>
  </article>
  <article class="abs feature" style="left:525px">
    <h3>Market Analysis</h3>
    <div class="art art-chart" role="img" aria-label="Illustration of a bar chart with magnifying glass"></div>
    <p>Lorem ipsum dolor sit amet, consectetur adipisicing elit, sed do eiusmod tempor incididunt ut labore et dolore magna aliqua. Ut enim ad minim veniam, quis nostrud</p>
    <span class="more">read more &gt;&gt;</span>
  </article>
  <article class="abs feature" style="left:764px">
    <h3>Corporate Value</h3>
    <div class="art art-team" role="img" aria-label="Photo of a business team"></div>
    <p>Lorem ipsum dolor sit amet, consectetur adipisicing elit, sed do eiusmod tempor incididunt ut labore et dolore magna aliqua. Ut enim ad minim veniam, quis nostrud</p>
    <span class="more">read more &gt;&gt;</span>
  </article>

  <section class="abs welcome">
    <h2 class="section-title">Welcome To Our Website</h2>
    <p>Lorem ipsum dolor sit amet, consectetur adipisicing elit, sed do eiusmod tempor incididunt ut labore et dolore magna aliqua. Ut enim ad minim veniam, quis nostrud exercitation ullamco laboris nisi ut aliquip ex ea commodo consequat. Duis aute irure dolor in reprehenderit in voluptate velit esse cillum dolore eu fugiat nulla pariatur. <a>Excepteur sint occaecat cupidatat non proident</a>, sunt in culpa qui officia deserunt mollit anim id est laborum.</p>
    <p>Lorem ipsum dolor sit amet, consectetur adipisicing elit, sed do eiusmod tempor incididunt ut labore et dolore magna aliqua. Ut enim ad minim veniam, quis nostrud exercitation ullamco laboris nisi ut aliquip ex ea commodo consequat. Duis aute irure dolor in reprehenderit in voluptate velit esse cillum dolore eu fugiat nulla pariatur. Excepteur sint occaecat cupidatat non proident, sunt in culpa qui officia deserunt mollit anim id est laborum.</p>
  </section>

  <aside class="abs testimonial">
    <h2 class="section-title">Testimonial</h2>
    <p class="quote"><span class="mark" style="left:0;top:-16px">&ldquo;</span>Lorem ipsum dolor sit amet, consectetur adipisicing elit, sed do eiusmod tempor incididunt ut labore et dolore magna aliqua. Ut enim ad minim veniam, quis nostrud exercitation ullamco laboris nisi ut aliquip.<span class="mark" style="right:4px;bottom:-18px">&rdquo;</span></p>
    <p class="author">- Admin</p>
  </aside>
</main>

<footer class="abs footer">
  <p class="links">Home &nbsp;|&nbsp; Services &nbsp;|&nbsp; Transfer &nbsp;|&nbsp; About us &nbsp;|&nbsp; Contact Us &nbsp;|&nbsp; FAQ</p>
  <p class="copy">All Right Reserved 2013.</p>
</footer>

</body>
</html>
```